Tour agency for FIT and groups need a business card design

We need a business card design for a tour agency company that is based in Perth called" BRISK NO", we aim to provide customise, unique and seamless travel arrangement for FIT and groups. We serve both high profile businessperson, government authorities, business partners, executives and investors. The name card should be more professional looking.
Updates

Project Deadline Extended Reason: Have some changes that needed to make, director will be back to office on Monday, sorry for the inconvenience cause. Added Saturday, May 6, 2017

Target Market(s)

High profile businessperson, government authorities, business partners, executives and investors.

Industry/Entity Type

Tourism

Contact Information for Business Card

Brisk NO
Level 1, 214 Marlowe Avenue, Dunreath NO, 6120
www.briskno.com.au

Font styles to use
Serif

Colors

Designer to choose colors to be used in the design.

Requirements
Must have
• My project must have a company logo
Nice to have
• a more professional and solid yet friendly name card design. We may want to include chinese name in the name card as well. Edge of the card can be filled with gold and we think that transparent name cards are interesting.

```html
<!DOCTYPE html>
<html lang="en">
<head>
<meta charset="UTF-8">
<title>Brisk NO – Business Card</title>
<link href="https://fonts.googleapis.com/css2?family=Open+Sans:wght@400&display=swap" rel="stylesheet">
<style>
  :root {
    --stage: #e9e7e4;
    --card-dark-top: #2c2a2b;
    --card-dark-bottom: #3d3b3c;
    --card-light: #ffffff;
    --ink-light: #f4f4f4;
    --ink-soft: #cfcdcd;
    --ink-dark: #1c1c1c;
    --rule: #8c8a8b;
  }
  * { margin: 0; padding: 0; box-sizing: border-box; }
  html, body {
    width: 1200px; height: 1200px; overflow: hidden;
    background: var(--stage);
    font-family: "Open Sans", Arial, sans-serif;
  }
  .stage {
    width: 1200px; height: 1200px;
    display: flex; flex-direction: column; align-items: center; justify-content: center;
    gap: 56px;
  }
  .card {
    width: 900px; height: 514px; position: relative;
    box-shadow: 0 6px 22px rgba(0,0,0,0.18);
  }
  /* Front */
  .card--front {
    background: linear-gradient(160deg, var(--card-dark-top), var(--card-dark-bottom));
    color: var(--ink-light);
  }
  .brand {
    position: absolute; display: flex; align-items: center; gap: 16px;
    letter-spacing: 2px;
  }
  .brand__dot { border-radius: 50%; flex: none; }
  .card--front .brand { left: 90px; top: 218px; font-size: 50px; }
  .card--front .brand__dot { width: 46px; height: 46px; background: var(--ink-light); }
  .details {
    position: absolute; left: 470px; top: 120px;
    display: flex; flex-direction: column; gap: 26px;
  }
  .details__group {
    border-left: 1.5px solid var(--rule);
    padding-left: 18px;
  }
  .person__name { font-size: 26px; letter-spacing: 1px; line-height: 1.2; }
  .person__role { font-size: 16px; color: var(--ink-soft); }
  .contact { list-style: none; font-size: 19px; line-height: 1.75; }
  .contact li { display: flex; align-items: center; gap: 12px; }
  .contact svg { width: 20px; height: 20px; flex: none; }
  .address { display: flex; gap: 12px; font-size: 19px; line-height: 1.6; }
  .address svg { width: 20px; height: 20px; margin-top: 5px; flex: none; }
  /* Back */
  .card--back { background: var(--card-light); color: var(--ink-dark); }
  .card--back .brand {
    left: 50%; top: 50%; transform: translate(-50%, -50%);
    font-size: 54px;
  }
  .card--back .brand__dot { width: 48px; height: 48px; background: var(--ink-dark); }
</style>
</head>
<body>
<main class="stage">
  <section class="card card--front" aria-label="Business card front">
    <div class="brand">
      <span class="brand__dot"></span>
      <span class="brand__name">BRISK NO</span>
    </div>
    <div class="details">
      <div class="details__group person">
        <p class="person__name">ALEX MARSH</p>
        <p class="person__role">Director</p>
      </div>
      <ul class="details__group contact">
        <li>
          <svg viewBox="0 0 20 20" fill="none" stroke="currentColor" stroke-width="1.6"><rect x="6" y="2" width="8" height="16" rx="1.5"/><line x1="8.5" y1="15" x2="11.5" y2="15"/></svg>
          123-555-0142
        </li>
        <li>
          <svg viewBox="0 0 20 20" fill="none" stroke="currentColor" stroke-width="1.4"><circle cx="10" cy="10" r="7.5"/><ellipse cx="10" cy="10" rx="3.2" ry="7.5"/><line x1="2.5" y1="10" x2="17.5" y2="10"/></svg>
          www.briskno.com.au
        </li>
        <li>
          <svg viewBox="0 0 20 20" fill="none" stroke="currentColor" stroke-width="1.5"><rect x="2" y="4.5" width="16" height="11"/><polyline points="2,4.5 10,11 18,4.5"/></svg>
          alex@briskno.com.au
        </li>
      </ul>
      <div class="details__group address">
        <svg viewBox="0 0 20 20" fill="currentColor"><polygon points="10,2 1,10 4,10 4,18 8,18 8,13 12,13 12,18 16,18 16,10 19,10"/></svg>
        <p>Level 1, 214 Marlowe Avenue<br>Dunreath NO, 6120</p>
      </div>
    </div>
  </section>

  <section class="card card--back" aria-label="Business card back">
    <div class="brand">
      <span class="brand__dot"></span>
      <span class="brand__name">BRISK NO</span>
    </div>
  </section>
</main>
</body>
</html>
```